Korvell Plant Services

We are a heavy diesel mechanical business with additional air con certificates, remapping engine rebuilt

Contact Information for Business Card

Company Name, Director Name, Managing Director, Contact details, email and website

Font styles to use
Serif
Script

```html
<!DOCTYPE html>
<html lang="en">
<head>
<meta charset="utf-8">
<title>Korvell Plant Services – Business Card</title>
<link rel="stylesheet" href="https://fonts.googleapis.com/css2?family=Open+Sans:wght@400;600;700&display=swap">
<style>
  :root {
    --page-bg: #d8d2ca;
    --card-bg: #ede8e1;
    --navy: #2d2b6b;
    --band: #2b2a68;
    --ink: #1c1c22;
    --text: #2a2a30;
    --address: #cfc7bd;
  }
  html, body {
    margin: 0;
    padding: 0;
    width: 1200px;
    height: 1047px;
    overflow: hidden;
    background: var(--page-bg);
    font-family: "Open Sans", Arial, sans-serif;
  }
  .business-card {
    position: absolute;
    left: 100px;
    top: 250px;
    width: 1000px;
    height: 547px;
    background: var(--card-bg);
    border-radius: 24px;
    overflow: hidden;
    box-shadow: 0 6px 24px rgba(0,0,0,0.12);
  }
  .card-band {
    position: absolute;
    inset: 0;
    width: 1000px;
    height: 547px;
  }
  .brand {
    position: absolute;
    left: 0;
    right: 0;
    top: 118px;
    display: flex;
    justify-content: center;
    align-items: center;
    gap: 18px;
  }
  .brand-dot {
    width: 44px;
    height: 44px;
    border-radius: 50%;
    background: var(--navy);
  }
  .brand-name {
    font-weight: 700;
    font-size: 46px;
    color: var(--navy);
    letter-spacing: -0.5px;
    line-height: 1;
  }
  .person {
    position: absolute;
    right: 556px;
    top: 308px;
    text-align: right;
  }
  .person-name {
    font-weight: 700;
    font-size: 34px;
    color: var(--navy);
    letter-spacing: 0.5px;
    line-height: 1.1;
  }
  .person-role {
    font-weight: 400;
    font-size: 23px;
    color: var(--text);
    margin-top: 6px;
  }
  .divider {
    position: absolute;
    left: 485px;
    top: 298px;
    width: 2px;
    height: 97px;
    background: var(--navy);
  }
  .contact-list {
    position: absolute;
    left: 524px;
    top: 298px;
    margin: 0;
    padding: 0;
    list-style: none;
  }
  .contact-item {
    display: flex;
    align-items: center;
    gap: 8px;
    font-size: 24px;
    color: var(--text);
    height: 33px;
  }
  .contact-icon {
    width: 22px;
    height: 22px;
    flex: none;
  }
  .address {
    position: absolute;
    left: 0;
    right: 0;
    top: 477px;
    text-align: center;
    font-size: 25px;
    color: var(--address);
  }
</style>
</head>
<body>
  <div class="business-card">
    <svg class="card-band" viewBox="0 0 1000 547" aria-hidden="true">
      <path d="M0 384 Q500 520 1000 378 L1000 547 L0 547 Z" fill="var(--band)"/>
      <path d="M55 378 Q500 478 962 374 Q500 496 55 378 Z" fill="var(--ink)"/>
    </svg>

    <div class="brand">
      <span class="brand-dot"></span>
      <span class="brand-name">Korvell Plant Services</span>
    </div>

    <div class="person">
      <div class="person-name">DANIEL HARTLEY</div>
      <div class="person-role">Managing Director</div>
    </div>

    <div class="divider"></div>

    <ul class="contact-list">
      <li class="contact-item">
        <svg class="contact-icon" viewBox="0 0 24 24" aria-hidden="true">
          <path d="M6.6 10.8a15.2 15.2 0 0 0 6.6 6.6l2.2-2.2a1 1 0 0 1 1-.25 11.4 11.4 0 0 0 3.6.57 1 1 0 0 1 1 1V20a1 1 0 0 1-1 1A17 17 0 0 1 3 4a1 1 0 0 1 1-1h3.5a1 1 0 0 1 1 1c0 1.25.2 2.45.57 3.57a1 1 0 0 1-.25 1z" fill="var(--navy)"/>
        </svg>
        123 456 789
      </li>
      <li class="contact-item">
        <svg class="contact-icon" viewBox="0 0 24 24" aria-hidden="true">
          <rect x="2" y="5" width="20" height="14" rx="2" fill="var(--navy)"/>
          <path d="M3 6.5l9 6.5 9-6.5" fill="none" stroke="var(--card-bg)" stroke-width="1.6"/>
        </svg>
        info@korvellplant.com
      </li>
      <li class="contact-item">
        <svg class="contact-icon" viewBox="0 0 24 24" aria-hidden="true">
          <circle cx="12" cy="12" r="10" fill="var(--navy)"/>
          <path d="M2 12h20M12 2c3 3 3 17 0 20M12 2c-3 3-3 17 0 20" fill="none" stroke="var(--card-bg)" stroke-width="1.3"/>
        </svg>
        www.yourwebsite.com
      </li>
    </ul>

    <div class="address">Your address, City State, Zip 1234</div>
  </div>
</body>
</html>
```